Law Firm Stationery Design - Traditional Meets Intuitive

Looking for a modern, yet classic, law firm stationery design. Simplicity is desired, but great ideas are encouraged. See attachment for company information. We utilize a variety of non-traditional legal tools to bring a different perspective to each of our client's particular situation. Final design should communicate classic values with intuitive, unique solutions.

Industry/Entity Type

Law Firm

Requirements
Should not have
• - No typical legal icons
• - No Tag Line!
• - DO NOT WANT WHAT WE ALREADY HAVE

```html
<!DOCTYPE html>
<html lang="en">
<head>
<meta charset="utf-8">
<title>Verenne Law LLC — Envelope</title>
<link href="https://fonts.googleapis.com/css2?family=Exo+2:wght@400&family=Open+Sans:wght@400&display=swap" rel="stylesheet">
<style>
  :root {
    --backdrop: #e9ece4;
    --paper: #ffffff;
    --brand-green: #8cc63f;
    --accent-grey: #9a9a9e;
    --name-grey: #a7a7a7;
    --ink: #4a4a4a;
  }
  html, body {
    margin: 0;
    width: 1200px;
    height: 1200px;
    overflow: hidden;
    background: var(--backdrop);
  }
  .canvas {
    position: relative;
    width: 1200px;
    height: 1200px;
  }
  .envelope {
    position: absolute;
    left: 60px;
    top: 350px;
    width: 1080px;
    height: 500px;
    background: var(--paper);
    box-shadow: 0 6px 24px rgba(0,0,0,0.12);
    overflow: hidden;
  }
  .edge-accent { position: absolute; }
  .edge-accent--left { left: 0; top: 0; width: 10px; height: 175px; background: var(--accent-grey); }
  .edge-accent--bottom-grey { left: 0; bottom: 0; width: 180px; height: 10px; background: var(--accent-grey); }
  .edge-accent--bottom-green { left: 180px; bottom: 0; right: 0; height: 10px; background: var(--brand-green); }

  .firm-name {
    position: absolute;
    left: 24px;
    top: 50px;
    margin: 0;
    font-family: "Exo 2", sans-serif;
    font-weight: 400;
    font-size: 50px;
    letter-spacing: 7px;
    color: var(--brand-green);
    text-transform: uppercase;
  }
  .person-name {
    position: absolute;
    left: 24px;
    top: 118px;
    margin: 0;
    font-family: "Open Sans", sans-serif;
    font-size: 28px;
    color: var(--name-grey);
  }
  .contact-row {
    position: absolute;
    left: 24px;
    bottom: 30px;
    display: flex;
    gap: 36px;
    font-family: "Open Sans", sans-serif;
    font-size: 15px;
    color: var(--ink);
  }
  .contact-item { position: relative; }
  .contact-icon {
    position: absolute;
    right: 0;
    top: -34px;
    width: 20px;
    height: 20px;
  }
</style>
</head>
<body>
<main class="canvas">
  <section class="envelope" aria-label="Verenne Law LLC envelope">
    <div class="edge-accent edge-accent--left"></div>
    <div class="edge-accent edge-accent--bottom-grey"></div>
    <div class="edge-accent edge-accent--bottom-green"></div>

    <h1 class="firm-name">Verenne Law LLC</h1>
    <p class="person-name">Example Name</p>

    <div class="contact-row">
      <span class="contact-item">
        <svg class="contact-icon" viewBox="0 0 20 20" aria-hidden="true">
          <path d="M10 1a6 6 0 0 0-6 6c0 4.5 6 11 6 11s6-6.5 6-11a6 6 0 0 0-6-6z" fill="#8cc63f"/>
          <circle cx="10" cy="7" r="2.2" fill="#fff"/>
        </svg>
        18 Harbor Lane, Suite 300 Dalton, MA 01226
      </span>
      <span class="contact-item">
        <svg class="contact-icon" viewBox="0 0 20 20" aria-hidden="true">
          <path d="M5 2c1 0 2 3 2 4s-1.5 1.5-1 3 3 4.5 4.5 5 2-1 3-1 4 1 4 2-1.5 3-3 3C8 18 2 12 2 5c0-1.5 2-3 3-3z" fill="#8cc63f"/>
        </svg>
        555-014-2700
      </span>
      <span class="contact-item">
        <svg class="contact-icon" viewBox="0 0 20 20" aria-hidden="true">
          <circle cx="10" cy="10" r="8.5" fill="#8cc63f"/>
          <path d="M1.5 10h17M10 1.5c-3 3-3 14 0 17M10 1.5c3 3 3 14 0 17" stroke="#fff" stroke-width="1.2" fill="none"/>
        </svg>
        www.verennelaw.com
      </span>
    </div>
  </section>
</main>
</body>
</html>
```